Brimvale OralNet IT Inc. new website

i need a website for my company which is dedicated to installation and service of computer systems in Dental Offices. I would like for it to encompass a technology feel and professional look. The company deals with all aspects of technology like, Audio Visual, computer systems and networks, Cloud services like data backup, data center. We provide manage services, support and services to Dental Professionals.

Looking for a Technology font but professional look Added Wednesday, April 20, 2016

Target Market(s)

Dental, Dentist

Industry/Entity Type

Dental

Number of Pages Required

5+ page

Font styles to use
Other font styles liked:
• Futuristic or Techy

Colors
0255a3
ec1f27

Requirements
Must have
• Tabs
Nice to have
• Have no idea maybe some suggestion on your part may help
Should not have
• A professional feel but have a techy look

```html
<!DOCTYPE html>
<html lang="en">
<head>
<meta charset="utf-8">
<title>Brimvale OralNet IT Inc.</title>
<link href="https://fonts.googleapis.com/css2?family=Open+Sans:ital,wght@0,400;0,600;0,700;1,400;1,600&display=swap" rel="stylesheet">
<style>
:root{
  --blue:#0255a3;
  --red:#ec1f27;
  --ink:#333333;
  --text:#555555;
  --grey-bg:#f2f2f2;
  --line:#e3e3e3;
  --white:#ffffff;
}
*{margin:0;padding:0;box-sizing:border-box}
html,body{width:1200px;height:2179px;overflow:hidden}
body{font-family:"Open Sans",Arial,sans-serif;color:var(--text);background:var(--white);position:relative}
.abs{position:absolute}

/* top bar */
.topbar{left:712px;top:0;width:488px;height:32px;background:var(--blue);clip-path:polygon(0 0,100% 0,100% 100%,14px 100%);color:var(--white);font-size:11px;display:flex;align-items:center;gap:26px;padding-left:32px}
.topbar span{display:flex;align-items:center;gap:6px}
.topbar svg{width:11px;height:11px;fill:var(--white)}

/* header */
.header{left:0;top:0;width:1200px;height:106px;border-bottom:1px solid var(--line)}
.brand{left:160px;top:44px;display:flex;align-items:center;gap:10px;font-weight:700;font-size:22px;color:var(--blue)}
.brand .mark{width:22px;height:22px;background:var(--blue);border-radius:3px}
.nav{left:452px;top:64px;font-size:11.5px;color:var(--ink);text-transform:uppercase}
.nav a{color:inherit;text-decoration:none;position:absolute;white-space:nowrap}
.nav a.active{color:var(--red)}
.search{left:1003px;top:57px;width:35px;height:35px;border-radius:50%;background:var(--red);display:flex;align-items:center;justify-content:center}
.search svg{width:13px;height:13px}

/* hero */
.hero{left:0;top:106px;width:1200px;height:511px;overflow:hidden;background:linear-gradient(100deg,#2d3640 0%,#414c58 40%,#5a6673 70%,#3b4550 100%)}
.hero-visual{left:574px;top:105px;width:460px;height:367px;border-radius:10px;background:radial-gradient(ellipse at 55% 45%,#e9eef3 0%,#b9c4cf 45%,rgba(90,102,115,0) 75%)}
.hero-title{left:160px;top:132px;color:var(--white);font-size:40px;font-weight:600;line-height:54px}
.hero-sub{left:160px;top:196px;width:370px;color:var(--white);font-style:italic;font-weight:600;font-size:16.5px;line-height:24px}
.hero-cta{left:163px;top:286px}
.arrow{top:346px;width:32px;height:32px;border:1.5px solid var(--white);border-radius:50%;display:flex;align-items:center;justify-content:center}
.arrow svg{width:10px;height:10px}
.hero .arrow{top:240px}

.btn{display:inline-flex;align-items:center;gap:5px;color:var(--white);font-size:11px;font-weight:700;text-transform:uppercase;height:32px;padding:0 14px;border-radius:2px}
.btn svg{width:10px;height:10px}
.btn.red{background:var(--red)}
.btn.blue{background:var(--blue)}

/* welcome */
.welcome-visual{left:174px;top:639px;width:313px;height:327px;background:radial-gradient(ellipse at 50% 50%,#3550c8 0%,#8a96b0 40%,#eceef2 70%,#ffffff 100%)}
.h2{font-size:24px;font-weight:700;color:var(--ink);text-transform:uppercase;letter-spacing:.2px}
.h2 em{font-style:normal;color:var(--red)}
.welcome-title{left:535px;top:648px}
.welcome-lead{left:535px;top:698px;width:505px;font-size:15px;line-height:22px;color:var(--blue);font-weight:600}
.welcome-body{left:535px;top:760px;width:510px;font-size:10.2px;line-height:19.5px;color:var(--text)}
.welcome-cta{left:535px;top:893px}

/* what we do */
.what{left:0;top:966px;width:1200px;height:400px;background:var(--grey-bg)}
.notch{left:580px;top:966px;width:0;height:0;border-left:22px solid transparent;border-right:22px solid transparent;border-top:22px solid var(--white)}
.what-title{left:0;top:1015px;width:1200px;text-align:center}
.feature{width:300px;height:90px}
.feature .icon{position:absolute;left:0;top:0;width:84px;height:84px;border-radius:50%;border:2px solid var(--blue);display:flex;align-items:center;justify-content:center}
.feature .icon i{display:flex;width:72px;height:72px;border-radius:50%;align-items:center;justify-content:center}
.feature .icon svg{width:36px;height:36px}
.feature.hot .icon{border-color:var(--red)}
.feature.hot .icon i{background:var(--red)}
.feature h3{position:absolute;left:101px;top:-10px;font-size:16.5px;font-weight:600;color:var(--ink);white-space:nowrap}
.feature p{position:absolute;left:101px;top:20px;width:175px;font-size:10.6px;line-height:19.5px;color:var(--text)}

/* services */
.services-title{left:0;top:1402px;width:1200px;text-align:center}
.services-intro{left:260px;top:1447px;width:680px;text-align:center;font-size:10.8px;line-height:20px;color:var(--ink)}
.card{top:1508px;width:276px;height:326px;border:1px solid var(--line);background:var(--white);text-align:center}
.card .photo{height:157px;width:100%}
.card h3{margin-top:15px;font-size:16.5px;font-weight:600;color:var(--ink)}
.card p{margin:10px auto 0;width:236px;font-size:10.6px;line-height:19.5px;color:var(--text)}
.card .btn{margin-top:19px}

/* footer */
.site-footer{color:var(--white)}
.footer{left:0;top:1874px;width:1200px;height:254px;background:var(--blue)}
.footer-brand{left:160px;top:1912px;width:175px;display:flex;align-items:flex-start;gap:10px;font-weight:700;font-size:18px;line-height:22px;color:var(--white)}
.footer-brand .mark{width:20px;height:20px;background:var(--white);border-radius:3px;flex:none;margin-top:1px}
.footer-about{left:160px;top:1973px;width:170px;font-size:10.8px;line-height:19.5px;color:var(--white)}
.col-rule{top:1916px;width:1px;height:140px;background:rgba(255,255,255,.18)}
.fh{font-size:16px;font-weight:600;text-transform:uppercase;color:var(--white)}
.fcol{top:1911px;color:var(--white)}
.fcol ul{list-style:none;margin-top:13px;font-size:11px;line-height:22.5px}
.contact li{display:flex;gap:10px;align-items:flex-start}
.contact svg{width:9px;height:9px;fill:var(--white);margin-top:6px;flex:none}
.news-note{font-size:11px;margin-top:4px}
.signup{margin-top:10px;display:flex;width:242px;height:32px;border:1px solid var(--white)}
.signup span{flex:1;background:var(--white);color:#888;font-size:10.5px;font-style:italic;padding-left:12px;display:flex;align-items:center}
.signup b{width:78px;background:var(--red);color:var(--white);font-size:11px;display:flex;align-items:center;justify-content:center;text-transform:uppercase}
.follow{margin-top:18px}
.social{display:flex;gap:6px;margin-top:10px}
.social i{width:28px;height:28px;border:1.5px solid var(--white);border-radius:50%}
.legal{left:0;top:2128px;width:1200px;height:51px;background:var(--red);color:var(--white);font-size:10.5px;display:flex;align-items:center;justify-content:center}
</style>
</head>
<body>

<header class="abs header">
  <div class="abs brand"><span class="mark"></span>Brimvale OralNet IT</div>
  <nav class="abs nav">
    <a class="active" style="left:0">Home</a>
    <a style="left:71px">Our Services</a>
    <a style="left:186px">About Us</a>
    <a style="left:283px">What We Do</a>
    <a style="left:394px">News</a>
    <a style="left:463px">Contact Us</a>
  </nav>
  <div class="abs search"><svg viewBox="0 0 16 16"><circle cx="6.5" cy="6.5" r="4.5" fill="none" stroke="#fff" stroke-width="2.2"/><path d="M10 10l4 4" stroke="#fff" stroke-width="2.4" stroke-linecap="round"/></svg></div>
</header>

<div class="abs topbar">
  <span><svg viewBox="0 0 16 16"><path d="M3 1l3 3-2 2c1 2 3 4 5 5l2-2 3 3-2 3C7 15 1 9 1 3z"/></svg>1-555-204-7710</span>
  <span><svg viewBox="0 0 16 16"><path d="M1 3h14v10H1z"/><path d="M1 3l7 6 7-6" stroke="#0255a3" stroke-width="1.2" fill="none"/></svg>hello@brimvale-oralnet.example</span>
  <span><svg viewBox="0 0 16 16"><circle cx="8" cy="5" r="3.5"/><path d="M1 15c0-4 3-6 7-6s7 2 7 6z"/></svg>Login</span>
</div>

<section class="abs hero">
  <div class="abs hero-visual" role="img" aria-label="Desktop computer showing a dental tooth model, with a stethoscope draped around it"></div>
  <h1 class="abs hero-title">Brimvale OralNet IT</h1>
  <p class="abs hero-sub">Installation and service of computer systems in Dental Offices. Accusantium doloremque lauda ntium totam rem aperiaea.</p>
  <div class="abs btn red hero-cta">Installation <svg viewBox="0 0 10 10"><circle cx="5" cy="5" r="5" fill="#fff"/><path d="M4 2.5L6.5 5 4 7.5" stroke="#ec1f27" stroke-width="1.6" fill="none"/></svg></div>
  <div class="abs arrow" style="left:40px"><svg viewBox="0 0 10 10"><path d="M6.5 1.5L3 5l3.5 3.5" stroke="#fff" stroke-width="1.6" fill="none"/></svg></div>
  <div class="abs arrow" style="left:1120px"><svg viewBox="0 0 10 10"><path d="M3.5 1.5L7 5 3.5 8.5" stroke="#fff" stroke-width="1.6" fill="none"/></svg></div>
</section>

<section class="welcome">
  <div class="abs welcome-visual" role="img" aria-label="Laptop showing error messages on screen, with a stethoscope resting on the keyboard"></div>
  <h2 class="abs h2 welcome-title">Welcome to <em>Brimvale OralNet IT</em></h2>
  <p class="abs welcome-lead">Sed ut perspiciatis unde omnis iste natus error sit voluptatem accus antium doloremque laudantium, totam rem aperiam.</p>
  <p class="abs welcome-body">Suasi architecto beatae vitae dicta sunt expli caboemo enim ipsam voluptatem quia voluptas sit asper naed ut perspiciatis unde omnis iste natus error sit voluptatem accusantium doloremque laudantium, totam rem aperiam, eaque ipsainventore veritatis et quasi architecto beatae vitae dicta sunt expli cab oemo enim ipsam voluptatem quia voluptas sit aspernad ut perspiciatis unde omnis iste natus error sit voluptatem accusantium doloremque laudantium, totam rem aperiam, eaque ipsainventore veritatisasi architecto beatae vitae dicta sunt expli caboemo enim ipsam voluptatem quia voluptas .</p>
  <div class="abs btn red welcome-cta">Read More <svg viewBox="0 0 10 10"><circle cx="5" cy="5" r="5" fill="#fff"/><path d="M4 2.5L6.5 5 4 7.5" stroke="#ec1f27" stroke-width="1.6" fill="none"/></svg></div>
</section>

<section class="abs what"></section>
<div class="abs notch"></div>
<h2 class="abs h2 what-title">What <em>We Do</em></h2>

<div class="abs feature hot" style="left:163px;top:1093px">
  <div class="icon"><i><svg viewBox="0 0 36 36" fill="#fff"><circle cx="14" cy="15" r="7"/><circle cx="14" cy="15" r="2.6" fill="#ec1f27"/><path d="M12 5h4v4h-4zM12 21h4v4h-4zM4 13h4v4H4zM20 13h4v4h-4z"/><circle cx="26" cy="26" r="4.5"/><circle cx="26" cy="26" r="1.6" fill="#ec1f27"/></svg></i></div>
  <h3>Technology</h3>
  <p>Sed ut perspiciatis unde omnis is te natus error sit voluptatem acc usantium doloremque laud</p>
</div>
<div class="abs feature" style="left:456px;top:1093px">
  <div class="icon"><i><svg viewBox="0 0 36 36" fill="#0255a3"><path d="M14 8l14-3v19h-3V10l-8 2v15h-3z"/><ellipse cx="11" cy="27" rx="4.5" ry="3.5"/><ellipse cx="24" cy="24" rx="4.5" ry="3.5"/></svg></i></div>
  <h3>Audio Visual</h3>
  <p>Sed ut perspiciatis unde omnis is te natus error sit voluptatem acc usantium doloremque laud</p>
</div>
<div class="abs feature" style="left:777px;top:1093px">
  <div class="icon"><i><svg viewBox="0 0 36 36" fill="#0255a3"><path d="M4 7h28v18H4z"/><path d="M7 10h22v12H7z" fill="#fff"/><path d="M15 25h6v4h4v2H11v-2h4z"/></svg></i></div>
  <h3>Computer Systems</h3>
  <p>Sed ut perspiciatis unde omnis is te natus error sit voluptatem acc usantium doloremque laud</p>
</div>
<div class="abs feature" style="left:163px;top:1218px">
  <div class="icon"><i><svg viewBox="0 0 36 36"><circle cx="18" cy="18" r="12" fill="#0255a3"/><path d="M12 11c3 1 5 3 4 6-2 1-4 0-5 3M20 24c1-3 4-3 5-6" stroke="#fff" stroke-width="2" fill="none"/></svg></i></div>
  <h3>Networks</h3>
  <p>Sed ut perspiciatis unde omnis is te natus error sit voluptatem acc usantium doloremque laud</p>
</div>
<div class="abs feature" style="left:456px;top:1218px">
  <div class="icon"><i><svg viewBox="0 0 36 36" fill="#0255a3"><path d="M10 27a6 6 0 0 1-1-12 8 8 0 0 1 15-3 6.5 6.5 0 0 1 3 15z"/></svg></i></div>
  <h3>Cloud Services</h3>
  <p>Sed ut perspiciatis unde omnis is te natus error sit voluptatem acc usantium doloremque laud</p>
</div>
<div class="abs feature" style="left:777px;top:1218px">
  <div class="icon"><i><svg viewBox="0 0 36 36" fill="#0255a3"><ellipse cx="18" cy="9" rx="10" ry="3.5"/><path d="M8 12c0 2 4.5 3.5 10 3.5S28 14 28 12v5c0 2-4.5 3.5-10 3.5S8 19 8 17z"/><path d="M8 20c0 2 4.5 3.5 10 3.5S28 22 28 20v5c0 2-4.5 3.5-10 3.5S8 27 8 25z"/></svg></i></div>
  <h3>Data Backup</h3>
  <p>Sed ut perspiciatis unde omnis is te natus error sit voluptatem acc usantium doloremque laud</p>
</div>

<section class="services">
  <h2 class="abs h2 services-title">Brimvale OralNet IT <em>Services</em></h2>
  <p class="abs services-intro">Sed ut perspiciatis unde omnis iste natus error sit voluptatem accusantium doloremque laudantium, totam rem aperiam, eaque ipsa inventore veritatis et quasi architecto beatae vitae dicta sunt explicaboemo enim ipsam voluptatem quia voluptas sit asperna</p>

  <article class="abs card" style="left:163px">
    <div class="photo" role="img" aria-label="Technician with a laptop in a server room" style="background:linear-gradient(120deg,#2a3a4d,#7d8fa3 55%,#dfe5ea)"></div>
    <h3>Manage Services</h3>
    <p>Sed ut perspiciatis undloreme omnis isssit olupt atem accusantiunde omniremqdptatem accusan tiunde omnireptatem accusantiun</p>
    <div class="btn red">Read More <svg viewBox="0 0 10 10"><circle cx="5" cy="5" r="5" fill="#fff"/><path d="M4 2.5L6.5 5 4 7.5" stroke="#ec1f27" stroke-width="1.6" fill="none"/></svg></div>
  </article>
  <article class="abs card" style="left:462px">
    <div class="photo" role="img" aria-label="Tooth model and dental mirror on a soft blue background" style="background:linear-gradient(120deg,#c9d6e3,#f3f6f9 55%,#b7c6d6)"></div>
    <h3>Support and Services</h3>
    <p>Sed ut perspiciatis undloreme omnis isssit olupt atem accusantiunde omniremqdptatem accusan tiunde omnireptatem accusantiun</p>
    <div class="btn blue">Read More <svg viewBox="0 0 10 10"><circle cx="5" cy="5" r="5" fill="#fff"/><path d="M4 2.5L6.5 5 4 7.5" stroke="#0255a3" stroke-width="1.6" fill="none"/></svg></div>
  </article>
  <article class="abs card" style="left:761px">
    <div class="photo" role="img" aria-label="Dentist and assistant reviewing an X-ray on a screen" style="background:linear-gradient(120deg,#3a4556,#9fb0c2 50%,#e7ecf1)"></div>
    <h3>Dental Professionals</h3>
    <p>Sed ut perspiciatis undloreme omnis isssit olupt atem accusantiunde omniremqdptatem accusan tiunde omnireptatem accusantiun</p>
    <div class="btn blue">Read More <svg viewBox="0 0 10 10"><circle cx="5" cy="5" r="5" fill="#fff"/><path d="M4 2.5L6.5 5 4 7.5" stroke="#0255a3" stroke-width="1.6" fill="none"/></svg></div>
  </article>
</section>

<footer class="site-footer">
  <div class="abs footer"></div>
  <div class="abs footer-brand"><span class="mark"></span><span>Brimvale OralNet IT</span></div>
  <p class="abs footer-about">Sed ut perspici loatis undloreme omnis isssit oluptat loem accus antiu ndeomniremqdptatem acc usan tiunde omnireptatem accusantiun</p>
  <div class="abs col-rule" style="left:350px"></div>
  <div class="abs col-rule" style="left:513px"></div>
  <div class="abs col-rule" style="left:757px"></div>

  <div class="abs fcol" style="left:388px">
    <div class="fh">Products</div>
    <ul><li>Alandit sed nulla</li><li>In ullamcorper</li><li>Est eget tempor</li><li>Cursus neque</li><li>Consectetuer</li></ul>
  </div>
  <div class="abs fcol contact" style="left:551px">
    <div class="fh">Contact Us</div>
    <ul style="font-size:10.5px;line-height:20px">
      <li><svg viewBox="0 0 10 10"><path d="M5 0a3.5 3.5 0 0 1 3.5 3.5C8.5 6 5 10 5 10S1.5 6 1.5 3.5A3.5 3.5 0 0 1 5 0z"/></svg><span>Postal address: PO Box 214,<br>Larkfield Office Park</span></li>
      <li><svg viewBox="0 0 10 10"><path d="M2 0l2 2-1 1.5c.7 1.4 1.8 2.5 3.5 3.5L8 6l2 2-1.5 2C4 10 0 6 0 1.5z"/></svg><span>Phone: 555-318-4406</span></li>
      <li><svg viewBox="0 0 10 10"><path d="M2 0h5v3H2zM0 3h10v5H0zM2 6h6v4H2z"/></svg><span>Fax: 555-318-4407</span></li>
      <li><svg viewBox="0 0 10 10"><path d="M0 2h10v6H0z"/></svg><span>hello@brimvale-oralnet.example</span></li>
    </ul>
  </div>
  <div class="abs fcol" style="left:795px">
    <div class="fh">Sign Up Newsletter</div>
    <p class="news-note">Please sign up here for latest deals</p>
    <div class="signup"><span>Email address</span><b>Sign Up</b></div>
    <div class="fh follow">Follow Us</div>
    <div class="social"><i></i><i></i><i></i><i></i><i></i></div>
  </div>
  <div class="abs legal">© 2016 BrimvaleOralNetIT.&nbsp; All right reserved&nbsp; Term of Use, Privacy Policy</div>
</footer>

</body>
</html>
```